High Quality fast food restaurant - Tomanyo

Tomanyo is a fast food company with its target's focused on logistic, simplicity, high quality, freshness and modern.

We need a web design where the customers can get a complete idea of our high quality completeness, we want to take fast food to a new upper level.

We would like to see the colours of wood and metal. Pictures have been attached of our local.

We would like to have something in similar to: http://www.qpz.example/
Updates

Images for the food we are going to sell can be found here: http://shrt.example/uWQa7

It will be the images with rice, french fries or pita bread.

Target Market(s)

The fast food eating people between sloppy food and restaurant level.

Industry/Entity Type

Fast Food Restaurant

Requirements
Should not have
• No Flash or Java

```html
<!DOCTYPE html>
<html lang="en">
<head>
<meta charset="utf-8">
<title>Tomanyo – High quality fastfood</title>
<link href="https://fonts.googleapis.com/css2?family=Arimo:ital,wght@0,400;1,400&family=Dancing+Script:wght@400&family=Italianno&family=Lato:wght@300&family=PT+Sans:ital,wght@0,400;1,400&display=swap" rel="stylesheet">
<style>
:root{
  --rust:#8a2c12;
  --rust-dark:#6e200c;
  --bar:#1f0f0a;
  --crimson:#8c0a0c;
  --crimson-light:#a8141a;
  --white:#ffffff;
  --text-red:#8e0b0d;
  --footer:#121212;
  --footer-text:#7b7b7b;
  --footer-title:#bdbdbd;
  --wood:#5a3a22;
}
*{margin:0;padding:0;box-sizing:border-box}
html,body{width:1200px;height:1148px;overflow:hidden;background:#fff}
h1,h2,h3,h4{font-weight:400}
.stage{position:relative;width:1200px;height:1148px;overflow:hidden}
.backdrop{position:absolute;inset:0;height:907px;
  background:linear-gradient(90deg,#f6b466 0%,#f2a252 8%,#e98f3f 13%,#c76a3a 40%,#d9a79a 80%,#efe0d6 88%,#f3e8de 100%)}
.header{position:absolute;left:155px;top:0;width:890px;height:113px;
  background:linear-gradient(180deg,#93321a,var(--rust) 60%,var(--rust-dark));
  box-shadow:0 3px 6px rgba(0,0,0,.35)}
.brand{position:absolute;left:18px;top:36px;display:flex;align-items:center;gap:10px;color:var(--white);font-family:"PT Sans",sans-serif}
.brand-mark{width:16px;height:16px;background:var(--white)}
.brand-name{font-size:32px;line-height:1}
.brand-tag{font-size:14px;margin-left:6px;opacity:.85;align-self:flex-end;padding-bottom:3px}
.search{position:absolute;left:572px;top:9px;width:304px;height:92px;border-radius:14px;
  background:linear-gradient(180deg,#6d4a2e,var(--wood) 50%,#3e2715);
  box-shadow:inset 0 0 0 3px #3a2514,0 2px 4px rgba(0,0,0,.4)}
.search-label{position:absolute;left:64px;top:10px;font-family:"Dancing Script",cursive;font-size:24px;color:var(--white);
  border-bottom:1px solid var(--white);line-height:1.05}
.search-field{position:absolute;left:62px;top:49px;width:168px;height:26px;background:#fff;
  font-family:"PT Sans",sans-serif;font-style:italic;font-size:11px;color:#999;padding:6px 6px}
.search-btn{position:absolute;left:230px;top:49px;width:23px;height:26px;background:#222;border:1px solid #777}
.nav{position:absolute;left:155px;top:131px;width:890px;height:48px;background:var(--bar);
  display:flex;align-items:center;padding-left:20px;font-family:"Dancing Script",cursive;font-size:18px;color:#fff;white-space:nowrap}
.nav a{color:#fff;text-decoration:none}
.nav .sep{margin:0 11px;font-family:Arial,sans-serif;font-size:17px}
.nav sup{font-size:11px}
.offer-tag{position:absolute;left:911px;top:127px;width:124px;height:76px;background:var(--crimson);
  transform:rotate(6deg);box-shadow:2px 3px 5px rgba(0,0,0,.45)}
.offer-tag::before{content:"";position:absolute;inset:5px;border:1px dashed #f2c7b8}
.offer-tag svg{position:absolute;left:42px;top:6px}
.offer-tag span{position:absolute;left:22px;top:44px;font-family:"Dancing Script",cursive;font-size:14px;color:#fff}
.hero{position:absolute;left:155px;top:178px;width:890px;height:330px;
  background:radial-gradient(ellipse at 58% 48%,#d9826a 0%,#c9b59a 18%,#e7e2da 40%,#bdb8b2 75%,#8f8a86 100%)}
.hero-box{position:absolute;left:46px;top:59px;width:334px;height:200px;background:rgba(90,90,90,.88);padding:16px 28px}
.hero-title{font-family:"Lato",sans-serif;font-weight:300;font-size:27px;color:#f3f3f3}
.hero-text{margin-top:10px;font-family:"Italianno",cursive;font-size:31px;line-height:28px;color:#f3f3f3}
.card{position:absolute;top:517px;width:284px;height:193px;background:#fff;box-shadow:0 2px 4px rgba(0,0,0,.3)}
.card-head{height:37px;background:linear-gradient(180deg,var(--crimson-light),var(--crimson));border-radius:4px 4px 0 0;
  font-family:"PT Sans",sans-serif;font-style:italic;font-size:17px;color:#fff;padding:8px 10px}
.card-photo{position:absolute;left:10px;top:47px;width:104px;height:136px;border:2px solid var(--crimson);
  background:linear-gradient(160deg,#7a3a3a,#b7c98a 35%,#90b760 60%,#dfe6d8)}
.card-text{position:absolute;left:122px;top:45px;width:156px;font-family:"Arimo",sans-serif;font-style:italic;font-size:14px;line-height:21.3px;color:var(--text-red)}
.more{position:absolute;right:10px;bottom:10px;font-family:"Arimo",sans-serif;font-style:italic;font-size:14px;color:var(--text-red)}
.more u{margin-right:4px}
.gallery{position:absolute;left:164px;top:728px;width:872px;height:169px;background:rgba(222,176,170,.8)}
.gallery-title{position:absolute;left:10px;top:7px;font-family:"Arimo",sans-serif;font-style:italic;font-size:15px;color:var(--text-red);text-decoration:underline}
.gallery-arrow{position:absolute;top:76px}
.thumb{position:absolute;top:37px;width:154px;height:122px;background:#fff;padding:4px}
.thumb div{width:100%;height:100%}
.food-a{background:linear-gradient(150deg,#6a8a2c,#d9d3c7 40%,#e7a23a 80%,#3a2a1a)}
.food-b{background:linear-gradient(150deg,#2e83c6,#e6e0d4 35%,#7a4a2c 60%,#d8c29a)}
.food-c{background:linear-gradient(180deg,#6b7a7c,#c9b79a 45%,#dcd5c9)}
.site-footer{position:absolute;left:0;top:907px;width:1200px;height:169px;background:var(--footer)}
.col{position:absolute;top:0;width:222px;padding-top:7px;height:160px}
.col + .col{border-left:1px solid #3a3a3a}
.col h4{font-family:"PT Sans",sans-serif;font-style:italic;font-size:16px;color:var(--footer-title);text-decoration:underline;margin:0 0 9px 10px}
.col li{list-style:none;font-family:"Arimo",sans-serif;font-style:italic;font-size:14px;color:var(--footer-text);line-height:25px}
.col li.active{color:#d8d8d8}
.col li.active span{text-decoration:underline}
.bottom{position:absolute;left:0;top:1076px;width:1200px;height:72px;background:#000;text-align:center}
.bottom-nav{padding-top:18px;font-family:"Arimo",sans-serif;font-size:13px;color:#fff}
.bottom-nav .sep{margin:0 11px}
.bottom-nav sup{font-size:9px}
.copy{margin-top:10px;font-family:"PT Sans",sans-serif;font-size:13px;color:#6a6a6a}
</style>
</head>
<body>
<div class="stage">
  <div class="backdrop" role="img" aria-label="Warm orange floral pattern on the left fading into a bowl of Asian dishes on the right"></div>

  <header class="header">
    <div class="brand">
      <span class="brand-mark"></span>
      <span class="brand-name">Tomanyo</span>
      <span class="brand-tag">High quality fastfood</span>
    </div>
    <form class="search">
      <div class="search-label">Search Here</div>
      <div class="search-field">Search Enter Store Here...</div>
      <div class="search-btn">
        <svg width="21" height="24" viewBox="0 0 21 24"><circle cx="12" cy="10" r="5" fill="none" stroke="#fff" stroke-width="2"/><line x1="8" y1="14" x2="4" y2="19" stroke="#fff" stroke-width="2.5"/></svg>
      </div>
    </form>
  </header>

  <nav class="nav">
    <a href="#">Menu</a><span class="sep">|</span>
    <a href="#">Fresh Offers</a><span class="sep">|</span>
    <a href="#">Qz<sup>®</sup> Club Card</a><span class="sep">|</span>
    <a href="#">Qz<sup>®</sup> Delivers</a><span class="sep">|</span>
    <a href="#">Company Information</a><span class="sep">|</span>
    <a href="#">Locations</a><span class="sep">|</span>
    <a href="#">Share</a>
  </nav>

  <section class="hero" role="img" aria-label="Plated seared fish with roasted vegetables and herbs">
    <div class="hero-box">
      <h1 class="hero-title">Lorem Ipsum is simply</h1>
      <p class="hero-text">Lorem Ipsum is simply dummy text of the printing and typesetting industry. Lorem Ipsum has been the industry</p>
    </div>
  </section>

  <div class="offer-tag">
    <svg width="40" height="34" viewBox="0 0 40 34"><path d="M8 22 C2 20 2 10 10 10 C12 3 26 3 29 9 C38 8 39 20 32 22 Z" fill="none" stroke="#fff" stroke-width="2"/><path d="M9 22 L9 28 L31 28 L31 22" fill="none" stroke="#fff" stroke-width="2"/></svg>
    <span>Special Offers</span>
  </div>

  <article class="card" style="left:164px">
    <h2 class="card-head">Dummy Title</h2>
    <div class="card-photo" role="img" aria-label="Fresh green salad"></div>
    <p class="card-text">Lorem Ipsum is simply dummy text of the printing and typesetting industry. Lorem Ipsum has been the industry</p>
    <a class="more"><u>READ MORE</u>»</a>
  </article>
  <article class="card" style="left:458px">
    <h2 class="card-head">Dummy Title</h2>
    <div class="card-photo" role="img" aria-label="Fresh green salad"></div>
    <p class="card-text">Lorem Ipsum is simply dummy text of the printing and typesetting industry. Lorem Ipsum has been the industry</p>
    <a class="more"><u>READ MORE</u>»</a>
  </article>
  <article class="card" style="left:752px">
    <h2 class="card-head">Dummy Title</h2>
    <div class="card-photo" role="img" aria-label="Fresh green salad"></div>
    <p class="card-text">Lorem Ipsum is simply dummy text of the printing and typesetting industry. Lorem Ipsum has been the industry</p>
    <a class="more"><u>READ MORE</u>»</a>
  </article>

  <section class="gallery">
    <h3 class="gallery-title">Restaurant Photo Gallary</h3>
    <svg class="gallery-arrow" style="left:11px" width="22" height="32" viewBox="0 0 22 32"><path d="M18 2 L6 16 L18 30" fill="none" stroke="var(--crimson)" stroke-width="5"/></svg>
    <div class="thumb" style="left:42px"><div class="food-a" role="img" aria-label="Kebab plate with fries and salad"></div></div>
    <div class="thumb" style="left:200px"><div class="food-b" role="img" aria-label="Meatballs on pita bread"></div></div>
    <div class="thumb" style="left:358px"><div class="food-c" role="img" aria-label="Stuffed pita sandwich"></div></div>
    <div class="thumb" style="left:517px"><div class="food-a" role="img" aria-label="Kebab plate with fries and salad"></div></div>
    <div class="thumb" style="left:675px"><div class="food-b" role="img" aria-label="Meatballs on pita bread"></div></div>
    <svg class="gallery-arrow" style="left:838px" width="22" height="32" viewBox="0 0 22 32"><path d="M4 2 L16 16 L4 30" fill="none" stroke="var(--crimson)" stroke-width="5"/></svg>
  </section>

  <footer class="site-footer">
    <div class="col" style="left:155px">
      <h4>Dummy Title</h4>
      <ul><li>» Lorem Ipsum is simply dummy</li><li>» Lorem Ipsum is simply dummy</li><li>» Lorem Ipsum is simply dummy</li><li>» Lorem Ipsum is simply dummy</li><li>» Lorem Ipsum is simply dummy</li></ul>
    </div>
    <div class="col" style="left:373px;padding-left:14px">
      <h4>Dummy Title</h4>
      <ul><li>» Lorem Ipsum is simply dummy</li><li class="active">» <span>Lorem Ipsum is simply dummy</span></li><li>» Lorem Ipsum is simply dummy</li><li>» Lorem Ipsum is simply dummy</li><li>» Lorem Ipsum is simply dummy</li></ul>
    </div>
    <div class="col" style="left:596px;padding-left:13px">
      <h4>Dummy Title</h4>
      <ul><li>» Lorem Ipsum is simply dummy</li><li>» Lorem Ipsum is simply dummy</li><li>» Lorem Ipsum is simply dummy</li><li>» Lorem Ipsum is simply dummy</li><li>» Lorem Ipsum is simply dummy</li></ul>
    </div>
    <div class="col" style="left:818px;padding-left:13px">
      <h4>Dummy Title</h4>
      <ul><li>» Lorem Ipsum is simply dummy</li><li>» Lorem Ipsum is simply dummy</li><li>» Lorem Ipsum is simply dummy</li><li>» Lorem Ipsum is simply dummy</li><li>» Lorem Ipsum is simply dummy</li></ul>
    </div>
  </footer>

  <div class="bottom">
    <div class="bottom-nav">
      Menu<span class="sep">|</span>Fresh Offers<span class="sep">|</span>Qz<sup>®</sup> Club Card<span class="sep">|</span>Qz<sup>®</sup> Delivers<span class="sep">|</span>Company Information<span class="sep">|</span>Locations<span class="sep">|</span>Share
    </div>
    <div class="copy">© Tomanyo. All rights reserved.</div>
  </div>
</div>
</body>
</html>
```